Business card and company logo design needed

Need a business card and company logo design for all stationary for an Aviation refueling consultancy business. Our business offers consulting services in the specialist aviation refueling industry. Services range from engineering, compliance and management consultancy through to project management services. This encompasses infrastructure from refinery through to airport and into the aircraft wing.

Design should be simple, 'less-is-more' concept, possibly taking advantage of the 'm' for tevlon and the fact is it the aviation industry. It should convey confidence, safety, experience, professionalism, aviation, engineering?, and should not be afraid to be simple in color...though please do not let this restrict your designs and imagination.

Target Market(s)

Airport authorities, oil majors, aircraft operators

Industry/Entity Type

Airport

Contact Information for Business Card

Tevlon Skyward Advisory Pty Ltd
Darius Tevlon
Director
mobile:+61427305158
email: darius@tevlonadvisory.example
Skype: darius.tevlonadvisory

Logo styles of interest
Emblem Logo
Pictorial/Combination Logo
Abstract Logo
Wordmark Logo
Lettermark Logo
Requirements
Must have
• - A feel of safety, security and confidence
Nice to have
• - Aviation has both heritage and modern 'sexy' elements so would be nice to try and capture both
- Aviation 'JET' fuel color is designated as black in signage or labels
- Themes? : Aviation fuel is derived from oil, it burns, safety, Jet fuel is colorless
- Company is global in reach, borderless like aircraft
Should not have
• - Cliche:

```html
<!DOCTYPE html>
<html lang="en">
<head>
<meta charset="utf-8">
<title>Tevlon Skyward Advisory – Business Card</title>
<link rel="stylesheet" href="https://fonts.googleapis.com/css2?family=Arimo:wght@400;700&family=Open+Sans:wght@400&display=swap">
<style>
  :root {
    --backdrop: #d9d9d9;
    --card: #ffffff;
    --card-edge: #2a0d12;
    --ink: #1a1a1a;
    --ink-soft: #8a8a8a;
    --accent-maroon: #4a1720;
    --accent-sky: #2ab0ec;
  }
  * { box-sizing: border-box; margin: 0; padding: 0; }
  html, body {
    width: 1200px;
    height: 1000px;
    overflow: hidden;
  }
  body {
    background: var(--backdrop);
    position: relative;
    font-family: "Open Sans", sans-serif;
    color: var(--ink);
  }
  .card {
    position: absolute;
    top: 230px;
    width: 330px;
    height: 540px;
    background: var(--card);
    border: 2px solid var(--card-edge);
    box-shadow: 0 6px 0 var(--accent-maroon), 0 14px 24px rgba(0, 0, 0, 0.18);
  }
  .card--back { left: 240px; }
  .card--front { left: 630px; }

  .role-block {
    position: absolute;
    top: 30px;
    left: 30px;
    font-family: "Arimo", sans-serif;
  }
  .role-title {
    font-size: 15px;
    color: var(--ink-soft);
    letter-spacing: 0.5px;
    border-bottom: 1px solid var(--ink-soft);
    padding-bottom: 1px;
  }
  .role-name {
    font-size: 17px;
    color: var(--ink);
    border-bottom: 1px solid var(--ink);
    padding-top: 1px;
    padding-bottom: 1px;
  }

  .contact-list {
    position: absolute;
    left: 0;
    right: 0;
    bottom: 40px;
    text-align: center;
  }
  .contact-item + .contact-item { margin-top: 14px; }
  .contact-label {
    font-family: "Arimo", sans-serif;
    font-weight: 700;
    font-size: 16px;
    color: var(--ink);
    line-height: 1.1;
  }
  .contact-label--skype { color: var(--accent-sky); font-weight: 400; }
  .contact-value {
    font-size: 17px;
    color: var(--ink);
    line-height: 1.25;
  }

  .brand {
    position: absolute;
    left: 0;
    right: 0;
    top: 250px;
    display: flex;
    flex-direction: column;
    align-items: center;
    gap: 16px;
  }
  .brand-dot {
    width: 26px;
    height: 26px;
    border-radius: 50%;
    background: var(--ink);
  }
  .brand-name {
    font-family: "Open Sans", sans-serif;
    font-size: 20px;
    font-weight: 400;
    color: var(--ink);
    text-align: center;
    line-height: 1.3;
    width: 250px;
  }
</style>
</head>
<body>
  <article class="card card--back" aria-label="Business card, contact side">
    <div class="role-block">
      <p class="role-title">DIRECTOR</p>
      <p class="role-name">Darius Tevlon</p>
    </div>
    <ul class="contact-list" style="list-style:none">
      <li class="contact-item">
        <p class="contact-label">TEL</p>
        <p class="contact-value">+61427305158</p>
      </li>
      <li class="contact-item">
        <p class="contact-label">E-MAIL</p>
        <p class="contact-value">darius@tevlonadvisory.example</p>
      </li>
      <li class="contact-item">
        <p class="contact-label contact-label--skype">SKYPE</p>
        <p class="contact-value">darius.tevlonadvisory</p>
      </li>
    </ul>
  </article>

  <article class="card card--front" aria-label="Business card, brand side">
    <div class="brand">
      <span class="brand-dot" aria-hidden="true"></span>
      <p class="brand-name">Tevlon Skyward Advisory Pty Ltd</p>
    </div>
  </article>
</body>
</html>
```